Non-profit organisation for street children in Indonesia

Lentera Bocah provides home, education, family and health care for street children and other underprivileged children in Indonesia.

We need an emotional catchy advertisement that will make people aware of the terrible living conditions of street children in Indonesia and the great work the Lentera Bocah Foundation is doing to help these children.

We have 1 photo available for this advertisement. A little girl laying in the streets. This photo can be used with a strong quote such as "Street children whose responsibility?" or "Safer out on streets than at home" or "This child doesn't have the right to have a childhood worth remembering?" or another strong quote. Be creative! It need to touch people!

See some similar advertisements of other non-profit organizations what we very much like:

http://7brightpix.example/wp-content/uploads/2011/07/boldposters41.jpg
http://7brightpix.example/wp-content/uploads/2011/07/affiches-nobles-motifs-058.jpg

Mission
To give every child in the world the opportunity to live a happy and healthy life free of poverty, exploitation, and violence.

Overview
Lentera Bocah Foundation is an independent non-governmental organisation founded in 2005 in the Netherlands and expanded to Indonesia in 2006. Our aim is to improve the lives of children and to protect their rights by providing education, accommodation, family care and medical and legal aid.

Description
Lentera Bocah (Light for Youngsters) Foundation serves homeless and impoverished children by offering them a new path in life. By providing them with the necessary shelter, education, and psychological support directed towards vocational training, mentorship, and micro-credit opportunities, it strives to enable their re-entery into the community as happy and self-sufficient adults.

Facts:
There are 70 million children in Indonesia, nearly 18 million are very poor and estimated 170,000 children live on the streets.

Pitch submissions need to be 960x696 pixels.

Files available 1 photo and logo
Updates

Reason: Dear Designers, We have decided to extend the deadline because we haven't received what we are after. Please make a design in the trend as the following two examples: http://7brightpix.example/wp-content/uploads/2011/07/boldposters41.jpg http://7brightpix.example/wp-content/uploads/2011/07/affiches-nobles-motifs-058.jpg We hope to receive a good design shortly! Thank you Kind regards Lentera Bocah

Target Market(s)

Everybody

Industry/Entity Type

Non-Profit

Requirements
Must have
• 1. A strong quote.
2. Website url: www.lenterabocah.org
3. Mission quote from Lentera Bocah:
Should not have
• To much text.

```html
<!DOCTYPE html>
<html lang="en">
<head>
<meta charset="utf-8">
<title>Lentera Bocah – He want to become a doctor</title>
<link rel="stylesheet" href="https://fonts.googleapis.com/css2?family=Jost:wght@300&family=Archivo:wght@800&family=Arimo:wght@400&display=swap">
<style>
  :root {
    --bg-green: #0f4a40;
    --headline-white: #ffffff;
    --brand-yellow: #ffd200;
    --panel-yellow: #ffd500;
    --panel-yellow-soft: rgba(255, 226, 80, 0.72);
    --ink: #3a3a2a;
    --photo-warm: #7a5a44;
    --photo-light: #e9e9e6;
    --photo-shade: #c4c8c3;
  }
  * { margin: 0; padding: 0; box-sizing: border-box; }
  html, body { width: 870px; height: 1200px; overflow: hidden; background: var(--bg-green); }
  .poster {
    position: relative;
    width: 870px;
    height: 1200px;
    background: var(--bg-green);
    overflow: hidden;
  }
  .brand {
    position: absolute;
    top: 58px;
    right: 56px;
    display: flex;
    align-items: center;
    gap: 10px;
    font-family: "Archivo", sans-serif;
    font-weight: 800;
    font-size: 22px;
    letter-spacing: 0.5px;
    color: var(--brand-yellow);
    text-transform: uppercase;
  }
  .brand-dot {
    width: 30px;
    height: 30px;
    border-radius: 50%;
    background: var(--brand-yellow);
  }
  .hero-photo {
    position: absolute;
    left: 94px;
    top: 260px;
    width: 682px;
    height: 940px;
    background:
      linear-gradient(90deg, var(--bg-green) 0%, rgba(15, 74, 64, 0) 18%, rgba(15, 74, 64, 0) 82%, var(--bg-green) 100%),
      linear-gradient(180deg, var(--bg-green) 0%, var(--photo-warm) 14%, var(--photo-warm) 26%, var(--photo-light) 44%, var(--photo-shade) 100%);
  }
  .headline {
    position: absolute;
    top: 276px;
    right: 58px;
    text-align: right;
    font-family: "Jost", sans-serif;
    font-weight: 300;
    font-size: 54px;
    line-height: 45px;
    color: var(--headline-white);
    text-transform: uppercase;
    letter-spacing: 0.3px;
  }
  .info-panel {
    position: absolute;
    left: 222px;
    top: 988px;
    width: 424px;
    height: 212px;
    display: flex;
  }
  .panel-question {
    width: 213px;
    background: var(--panel-yellow-soft);
    padding: 20px 16px 0 0;
    text-align: right;
    font-family: "Archivo", sans-serif;
    font-weight: 800;
    font-size: 14px;
    line-height: 15px;
    letter-spacing: 0.8px;
    color: var(--ink);
    text-transform: uppercase;
  }
  .panel-mission {
    flex: 1;
    background: var(--panel-yellow);
    padding: 18px 14px 0 17px;
    font-family: "Arimo", sans-serif;
    color: var(--ink);
  }
  .mission {
    font-size: 15px;
    line-height: 16.6px;
  }
  .donate {
    margin-top: 17px;
    font-size: 9.6px;
    line-height: 11px;
  }
</style>
</head>
<body>
<main class="poster">
  <div class="brand"><span class="brand-dot"></span>Lentera Bocah</div>

  <div class="hero-photo" role="img" aria-label="Photo of a young boy in an oversized white doctor's coat holding up a stethoscope"></div>

  <h1 class="headline">He want<br>to become<br>a doctor</h1>

  <section class="info-panel">
    <p class="panel-question">Street<br>children<br>whose<br>responsibility?</p>
    <div class="panel-mission">
      <p class="mission">To give every child in the world the opportunity to live a happy and healthy life free of poverty, exploitation, and violence.</p>
      <p class="donate">Donate to<br>GIRO 4725 t.a.v. Stichting Lentera Bocah<br>or financial adopt a child on<br>www.lenterabocah.org</p>
    </div>
  </section>
</main>
</body>
</html>
```